International Parcel Forwarder needs website redesign and logo

We need an updated website design to make our existing site look more modern, global and trustworthy. Current site
www.parvento.com -- we do not want to rebuild headers or at this point do copyright we are simply looking to make the site pop:)
The service we provide is for shoppers living outside the USA looking to shop here and save money on shipping or get access to stores that won't ship internationally or accept international payment.
Target Market(s)
Online shoppers living outside the USA
Industry/Entity Type
Shipping
Logo Text
US shopping, global shipping
Coding
Coded - Design and coding required
Number of Pages Required
5+ page
Font styles to use

```html
<!DOCTYPE html>
<html lang="en">
<head>
<meta charset="utf-8">
<title>Parvento – US shopping, global shipping</title>
<link rel="stylesheet" href="https://fonts.googleapis.com/css2?family=Open+Sans:wght@400;600;700;800&display=swap">
<style>
:root{
  --navy:#2f3d7e;
  --navy-dark:#27336b;
  --nav:#3b4b94;
  --orange:#f29a1f;
  --blue-btn:#4a7fd0;
  --ink:#333;
  --muted:#666;
  --panel:#ececec;
  --line:#9aa3c7;
  --white:#fff;
}
*{box-sizing:border-box;margin:0;padding:0}
html,body{width:678px;height:1200px;overflow:hidden}
body{font-family:"Open Sans",Arial,sans-serif;color:var(--ink);background:var(--white);position:relative}

.site-header{height:63px;background:linear-gradient(180deg,#34438a,var(--navy-dark));position:relative}
.brand{position:absolute;left:14px;top:8px;color:var(--orange);font-weight:800;font-size:24px;display:flex;align-items:center;gap:6px;letter-spacing:.5px}
.brand-dot{width:14px;height:14px;border-radius:50%;background:var(--orange)}
.brand-tag{position:absolute;left:34px;top:38px;font-size:9px;color:#dfe4f5}
.account{position:absolute;right:16px;top:14px;display:flex;gap:8px}
.account a{font-size:11px;color:var(--white);text-decoration:none;padding:4px 10px;border-radius:3px}
.btn-login{background:var(--blue-btn)}
.btn-signup{background:var(--orange)}

.main-nav{height:24px;background:var(--nav);display:flex;justify-content:flex-end;align-items:center;gap:24px;padding-right:18px}
.main-nav a{color:var(--white);font-size:11px;font-weight:700;text-decoration:none}

.hero{height:203px;background:linear-gradient(120deg,#d9d3c4 0%,#c9b08a 45%,#9c7a52 75%,#e8e4dc 100%);position:relative}
.hero-caption{position:absolute;left:14px;top:50px;width:240px;padding:12px 14px;background:rgba(255,255,255,.35);color:var(--white);font-size:14px;font-weight:600;line-height:1.35}
.hero-dots{position:absolute;right:16px;bottom:10px;display:flex;gap:6px}
.hero-dots span{width:7px;height:7px;border-radius:50%;background:var(--white)}

.section-title{display:flex;align-items:center;gap:12px;justify-content:center;color:var(--navy);font-weight:700;font-size:15px;letter-spacing:.5px}
.section-title::before,.section-title::after{content:"";height:1px;width:170px;background:var(--line)}

.how{background:var(--panel);height:325px;padding-top:16px;position:relative}
.how-map{position:absolute;left:60px;top:44px;width:560px;height:92px;background:linear-gradient(90deg,#c9d5ef,#b4c4e8,#c9d5ef);border-radius:40px;opacity:.8}
.steps{position:absolute;left:100px;top:62px;width:480px;display:flex;justify-content:space-between}
.steps::before{content:"";position:absolute;left:30px;right:30px;top:30px;border-top:2px dashed var(--navy)}
.step{width:60px;height:60px;border-radius:50%;background:var(--navy);display:flex;align-items:center;justify-content:center;position:relative}

.welcome{position:absolute;left:44px;top:170px;width:340px;height:130px;background:#dcdcdc;text-align:center;padding-top:18px}
.welcome h2{font-weight:400;font-size:24px;color:#222}
.welcome p{font-size:12px;margin:10px 0 12px}
.btn-cta{display:inline-block;background:var(--orange);color:#333;font-size:11px;padding:5px 30px;border-radius:3px;text-decoration:none}
.video{position:absolute;left:396px;top:167px;width:220px;height:138px;background:linear-gradient(160deg,#6aa8e0,#9fd0a0 60%,#e6b86a);border:3px solid #111}
.video-bar{height:20px;background:rgba(0,0,0,.75);color:var(--white);font-size:10px;padding:3px 8px}

.why{padding-top:22px;height:292px}
.features{display:grid;grid-template-columns:1fr 1fr;gap:22px 30px;padding:24px 60px 0 130px}
.feature{display:flex;gap:14px;position:relative}
.feature-photo{flex:none;width:56px;height:56px;border-radius:50%;background:radial-gradient(circle at 40% 40%,#8fb0dc,#33528f)}
.feature h3{font-size:12px;color:var(--navy);font-weight:700;margin-bottom:4px}
.feature ul{list-style:none;font-size:10px;color:var(--muted)}
.feature li{position:relative;padding-left:10px;line-height:1.35}
.feature li::before{content:"";position:absolute;left:0;top:5px;width:4px;height:4px;border-radius:50%;background:#333}
.features .feature:nth-child(odd){margin-left:-70px}
.badge{position:absolute;right:-40px;bottom:-10px;width:20px;height:26px;background:var(--navy);border-radius:2px}

.retailers{display:grid;grid-template-columns:repeat(4,1fr);row-gap:32px;padding:20px 60px 0;height:220px;align-items:center;text-align:center}
.retailer{font-family:"Open Sans",Arial,sans-serif;font-weight:700;font-size:17px;color:#222}

.site-footer{position:absolute;left:0;bottom:0;width:678px;height:70px;background:var(--navy)}
.footer-links{display:flex;justify-content:center;gap:20px;padding-top:10px}
.footer-links a{color:var(--white);font-size:9px;text-decoration:none}
.carriers{display:flex;justify-content:center;gap:22px;margin-top:14px}
.carriers span{font-size:9px;font-weight:700;color:#aeb6d8}
.copyright{position:absolute;right:12px;bottom:8px;font-size:8px;color:#cdd3ea}
</style>
</head>
<body>
<header class="site-header">
  <div class="brand"><span class="brand-dot"></span>PARVENTO</div>
  <div class="brand-tag">US shopping, global shipping</div>
  <div class="account"><a class="btn-login" href="#">Log In</a><a class="btn-signup" href="#">Sign Up</a></div>
</header>
<nav class="main-nav">
  <a href="#">Shipping Calculator</a><a href="#">How It Works</a><a href="#">Parvento Pricing</a><a href="#">Contact Us</a><a href="#">Learn More ▾</a><a href="#">Blog</a>
</nav>

<section class="hero" role="img" aria-label="Stacked cardboard parcels on a hand truck">
  <div class="hero-caption">Shop At Any U.S. Retailer<br>Ship Anywhere.</div>
  <div class="hero-dots"><span></span><span></span><span></span></div>
</section>

<section class="how">
  <h2 class="section-title">HOW PARVENTO WORKS</h2>
  <div class="how-map" role="img" aria-label="World map backdrop"></div>
  <div class="steps">
    <div class="step"><svg width="30" height="20" viewBox="0 0 30 20"><rect width="30" height="20" fill="#fff"/><g fill="#c0392b"><rect y="2" width="30" height="2"/><rect y="7" width="30" height="2"/><rect y="12" width="30" height="2"/><rect y="17" width="30" height="2"/></g><rect width="13" height="10" fill="#2f3d7e"/></svg></div>
    <div class="step"><svg width="30" height="26" viewBox="0 0 30 26" fill="none" stroke="#fff" stroke-width="2.5"><path d="M1 3h5l4 14h15l3-10H8"/><circle cx="12" cy="22" r="2" fill="#fff"/><circle cx="23" cy="22" r="2" fill="#fff"/></svg></div>
    <div class="step"><svg width="30" height="28" viewBox="0 0 30 28" fill="#fff"><path d="M15 1 1 14h4v13h8v-8h4v8h8V14h4z"/></svg></div>
    <div class="step"><svg width="32" height="28" viewBox="0 0 32 28" fill="#fff"><path d="M31 12c0-1.5-1.5-2-3-2h-7L13 0h-3l4 10H7L4 6H1l2 8-2 8h3l3-4h7l-4 10h3l8-10h7c1.5 0 3-.5 3-2z"/></svg></div>
  </div>
  <div class="welcome">
    <h2>Welcome</h2>
    <p>Sign in the best shipping website</p>
    <a class="btn-cta" href="#">Sign in now</a>
  </div>
  <div class="video" role="img" aria-label="Explainer video still of a cartoon shopper opening a parcel">
    <div class="video-bar">How Parvento Works</div>
  </div>
</section>

<section class="why">
  <h2 class="section-title">WHY USE PARVENTO</h2>
  <div class="features">
    <div class="feature"><div class="feature-photo" role="img" aria-label="Globe with shipping routes"></div><div><h3>EXPERIENCE</h3><ul><li>30 years experience in international shipping</li></ul></div></div>
    <div class="feature"><div class="feature-photo" role="img" aria-label="Cargo crane at a port"></div><div><h3>VALUE</h3><ul><li>Discounted shipping rates with major carriers</li><li>No membership or joining fees</li><li>Low consolidation fees</li></ul></div></div>
    <div class="feature"><div class="feature-photo" role="img" aria-label="Handshake"></div><div><h3>TRUST</h3><ul><li>Excellent customer service</li><li>A+ rating from the Consumer Trust Council</li></ul></div></div>
    <div class="feature"><div class="feature-photo" role="img" aria-label="City skyline"></div><div><h3>SAVINGS</h3><ul><li>No fees to receive packages</li><li>No U.S. sales tax when using our New Alder warehouse</li><li>45 days free storage</li></ul></div><span class="badge" aria-hidden="true"></span></div>
  </div>
</section>

<section class="retailers">
  <span class="retailer">Marlow's</span><span class="retailer">rivora</span><span class="retailer">ALWAYS 19</span><span class="retailer">CITY GLOW</span>
  <span class="retailer">NORTHFIELD</span><span class="retailer">GOOD DEAL</span><span class="retailer">KIV</span><span class="retailer">bidly</span>
  <span class="retailer">PLAYMORE</span><span class="retailer">jane hollow</span><span class="retailer">ARC</span><span class="retailer">Craftly</span>
</section>

<footer class="site-footer">
  <div class="footer-links"><a href="#">How it works</a><a href="#">Pricing</a><a href="#">Terms</a><a href="#">Privacy Policy</a><a href="#">Contact Us</a></div>
  <div class="carriers"><span>Swiftpost</span><span>Postline</span><span>Aeroship</span></div>
  <div class="copyright">© 2017 parvento.com</div>
</footer>
</body>
</html>
```